Baby Girl Nora Birth Announcement for Dec 1st 2020

Using an existing photo from an artist, build a 2 sided card with messaging and details on opposite side.

Style: fun, timeless, elegant, vibrant
Side 1:
Text "Welcome Nora".
Use file called FRONT BACKGROUND - Welcome Nora.
Consider 2 fonts, consider 2 colors of words. use provided image and monochromatic image of a heart
Side 2 content to be fit:
"Welcome to our little ray of light!"
"Nora Jade Ruth Pelkey"
Date of birth ---/--/----
Time of birth
Weight
Length
"Loving and Proud Parents : Greta Pelkey - Ter Hoorwijk & Daniel Pelkey"
Amazing and Wonderful God Parents : "Leimomi Kahue & Bastien De Kerckhove" + "Mina Ling Ashcombe & Grant Ashcombe "

Target Market(s)

Family and friends.
International audience (european/asian/american).
Urban, up market,

Requirements
Must have
• Use file called FRONT BACKGROUND - Welcome Nora on the front
Nice to have
• Consider 2 fonts, consider 2 colors of words. use provided image and monochromatic image of a heart

```html
<!DOCTYPE html>
<html lang="en">
<head>
<meta charset="utf-8">
<title>Welcome Nora – Birth Announcement</title>
<link rel="stylesheet" href="https://fonts.googleapis.com/css2?family=Parisienne&family=Lora:ital,wght@1,500&family=Poppins:ital,wght@0,400;0,500;1,500&display=swap">
<style>
  :root {
    --stage: #f4e3e7;
    --card: #ffffff;
    --front-warm: #f6e7b8;
    --front-glow: #fffdf6;
    --front-green: #c9d3a3;
    --photo-dark: #5a5a5a;
    --photo-light: #d8d8d8;
    --ink-dark: #262626;
    --ink-grey: #5b5b5b;
    --ink-teal: #1f3f48;
    --ink-soft: #8a8a8a;
    --pattern: #ececec;
  }
  * { box-sizing: border-box; margin: 0; padding: 0; }
  html, body { width: 1200px; height: 1200px; overflow: hidden; }
  body { background: var(--stage); position: relative; font-family: "Poppins", sans-serif; }

  .card {
    position: absolute;
    background: var(--card);
    box-shadow: 0 4px 18px rgba(120, 40, 60, 0.18);
    overflow: hidden;
  }

  /* Front side */
  .card--front { left: 39px; top: 68px; width: 781px; height: 507px; }
  .front-backdrop {
    position: absolute; inset: 0;
    background:
      radial-gradient(ellipse 40% 45% at 80% 40%, var(--front-glow) 0%, rgba(255,253,246,0) 70%),
      radial-gradient(ellipse 55% 50% at 72% 45%, var(--front-warm) 0%, rgba(246,231,184,0) 75%),
      linear-gradient(180deg, #fbfaf4 0%, var(--front-green) 48%, #f7f6f2 68%, #fbfbf9 100%);
  }
  .baby-photo {
    position: absolute; left: 28px; top: 68px; width: 403px; height: 371px;
    background: linear-gradient(135deg, var(--photo-light) 0%, #a9a9a9 45%, var(--photo-dark) 100%);
    box-shadow: 0 2px 8px rgba(0,0,0,0.3);
  }
  .front-greeting {
    position: absolute; left: 451px; top: 262px;
    font-family: "Parisienne", cursive; font-size: 62px; line-height: 1;
    color: var(--ink-dark);
  }
  .front-name {
    position: absolute; left: 480px; top: 330px;
    font-family: "Parisienne", cursive; font-size: 118px; line-height: 1;
    color: var(--ink-grey);
  }

  /* Back side */
  .card--back { left: 333px; top: 593px; width: 780px; height: 506px; }
  .back-pattern {
    position: absolute; inset: 0;
    background: linear-gradient(180deg, #fafafa 0%, var(--card) 50%, #fafafa 100%);
    border: 1px solid var(--pattern);
  }
  .back-content {
    position: absolute; inset: 0; text-align: center;
  }
  .back-tagline {
    position: absolute; left: 0; right: 0; top: 150px;
    font-family: "Parisienne", cursive; font-size: 29px; color: var(--ink-soft);
  }
  .back-name {
    position: absolute; left: 0; right: 0; top: 195px;
    font-family: "Lora", serif; font-style: italic; font-weight: 500;
    font-size: 42px; color: var(--ink-teal);
  }
  .birth-details {
    position: absolute; left: 0; right: 0; top: 265px;
    font-size: 12px; font-weight: 500; letter-spacing: 3.2px; color: var(--ink-dark);
    word-spacing: 6px;
  }
  .credit-heading {
    position: absolute; left: 0; right: 0;
    font-size: 13px; font-weight: 500; color: var(--ink-dark);
  }
  .credit-heading--parents { top: 375px; font-style: italic; }
  .credit-heading--godparents { top: 423px; }
  .credit-names {
    position: absolute; left: 0; right: 0;
    font-size: 12px; color: var(--ink-soft);
  }
  .credit-names--parents { top: 396px; }
  .credit-names--godparents { top: 444px; }
</style>
</head>
<body>
  <section class="card card--front">
    <div class="front-backdrop" role="img" aria-label="Sunlit photograph of a glittering unicorn toy figure in soft warm light"></div>
    <div class="baby-photo" role="img" aria-label="Black and white photograph of the sleeping newborn with a knitted toy"></div>
    <div class="front-greeting">Welcome</div>
    <div class="front-name">Nora</div>
  </section>

  <section class="card card--back">
    <div class="back-pattern" role="img" aria-label="Soft grey pattern of small hearts on dotted vertical strings"></div>
    <div class="back-content">
      <p class="back-tagline">Welcome to our little ray of light</p>
      <h1 class="back-name">Nora Jade Ruth Pelkey</h1>
      <p class="birth-details">01/12/2020 &nbsp;| &nbsp;12:00 AM &nbsp;| &nbsp;3500 GRAM &nbsp;| &nbsp;55 CM</p>
      <p class="credit-heading credit-heading--parents">~ Loving and Proud Parents ~</p>
      <p class="credit-names credit-names--parents">Greta Pelkey - Ter Hoorwijk &amp; Daniel Pelkey</p>
      <p class="credit-heading credit-heading--godparents">~ Amazing and Wonderful God Parents ~</p>
      <p class="credit-names credit-names--godparents">Leimomi Kahue &amp; Bastien De Kerckhove + Mina Ling Ashcombe &amp; Grant Ashcombe</p>
    </div>
  </section>
</body>
</html>
```